Criação de Papelaria Profissional para Construção & Engenharia
" Fabricamos estruturas metálicas para Armazéns Graneleiros, Unidades de Beneficiamento de Sementes, Garagem para máquinas agrícolas, Classificação, etc "

```html
<!DOCTYPE html>
<html lang="pt-BR">
<head>
<meta charset="utf-8">
<title>Papel timbrado – Valdran Metalurgia e Engenharia</title>
<link href="https://fonts.googleapis.com/css2?family=Arimo:wght@400;700&display=swap" rel="stylesheet">
<style>
  :root {
    --stage: #e9e7e4;
    --paper: #ffffff;
    --brand-red: #e3141c;
    --ink: #1a1a1a;
    --ink-soft: #333333;
    --watermark: rgba(227, 20, 28, 0.12);
  }
  * { box-sizing: border-box; margin: 0; padding: 0; }
  html, body {
    width: 1200px; height: 1200px; overflow: hidden;
    background: var(--stage);
    font-family: "Arimo", Arial, sans-serif;
    color: var(--ink);
  }
  .letterhead {
    position: absolute; left: 210px; top: 35px;
    width: 780px; height: 1130px;
    background: var(--paper);
    box-shadow: 0 6px 24px rgba(0,0,0,0.18);
    overflow: hidden;
  }
  .brand {
    position: absolute; top: 52px; left: 0; width: 100%;
    text-align: center; color: var(--brand-red); font-weight: 700;
  }
  .brand-name { font-size: 40px; letter-spacing: 2px; line-height: 1; }
  .brand-tagline { font-size: 13px; letter-spacing: 1.5px; margin-top: 4px; text-transform: uppercase; }
  .doc-title {
    position: absolute; top: 232px; left: 0; width: 100%;
    text-align: center; font-size: 38px; font-weight: 400; letter-spacing: 1px;
  }
  .body-copy {
    position: absolute; top: 308px; left: 100px; width: 580px;
    font-size: 12.6px; line-height: 1.72; color: var(--ink-soft);
  }
  .body-copy p { margin-bottom: 26px; }
  .watermark {
    position: absolute; top: 600px; left: 0; width: 100%;
    text-align: center; color: var(--watermark); font-weight: 700;
  }
  .watermark-name { font-size: 74px; letter-spacing: 4px; line-height: 1; }
  .watermark-tagline { font-size: 26px; letter-spacing: 3px; text-transform: uppercase; }
  .signature {
    position: absolute; top: 968px; left: 245px; width: 180px; height: 70px;
  }
  .signature-mark {
    position: absolute; left: 0; top: 0; width: 110px; height: 64px;
    background: linear-gradient(120deg, rgba(0,0,0,0.05), rgba(0,0,0,0.14));
    border-radius: 30px;
  }
  .signature-name {
    position: absolute; left: 86px; top: 46px; font-size: 11px; font-weight: 700; white-space: nowrap;
  }
  .signature-role {
    position: absolute; left: 132px; top: 60px; font-size: 10px; color: var(--brand-red);
  }
  .contact {
    position: absolute; top: 1052px; left: 70px; width: 640px;
    display: flex; justify-content: space-between; align-items: center;
    font-size: 11px; font-weight: 700; line-height: 1.3; color: var(--ink);
  }
  .contact-item { display: flex; align-items: center; gap: 8px; }
  .contact-item svg { width: 20px; height: 20px; fill: var(--brand-red); flex: none; }
  .footer-band { position: absolute; left: 0; bottom: 0; width: 100%; height: 52px; }
</style>
</head>
<body>
  <main class="letterhead">
    <header class="brand">
      <div class="brand-name">VALDRAN</div>
      <div class="brand-tagline">Metalurgia e Engenharia</div>
    </header>

    <h1 class="doc-title">TÍTULO</h1>

    <div class="watermark" aria-hidden="true">
      <div class="watermark-name">VALDRAN</div>
      <div class="watermark-tagline">Metalurgia e Engenharia</div>
    </div>

    <section class="body-copy">
      <p>Lorem Ipsum é simplesmente uma simulação de texto da indústria tipográfica e de impressos, e vem sendo utilizado desde o século XVI, quando um impressor desconhecido pegou uma bandeja de tipos e os embaralhou para fazer um livro de modelos de tipos. Lorem Ipsum sobreviveu não só a cinco séculos, como também ao salto para a editoração eletrônica, permanecendo essencialmente inalterado. Se popularizou na década de 60, quando a Letraset lançou decalques contendo passagens de Lorem Ipsum, e mais recentemente quando passou a ser integrado a softwares de editoração eletrônica como Aldus PageMaker.</p>
      <p>Lorem Ipsum é simplesmente uma simulação de texto da indústria tipográfica e de impressos, e vem sendo utilizado desde o século XVI, quando um impressor desconhecido pegou uma bandeja de tipos e os embaralhou para fazer um livro de modelos de tipos. Lorem Ipsum sobreviveu não só a cinco séculos, como também ao salto para a editoração eletrônica, permanecendo essencialmente inalterado. Se popularizou na década de 60, quan</p>
      <p>Lorem Ipsum é simplesmente uma simulação de texto da indústria tipográfica e de impressos, e vem sendo utilizado desde o século XVI, quando um impressor desconhecido pegou uma bandeja de tipos e os embaralhou para fazer</p>
      <p>Lorem Ipsum é simplesmente uma simulação de texto da indústria tipográfica e de impressos, e vem sendo utilizado desde o século XVI, quando um impressor desconhecido pegou uma bandeja de tipos e os embaralhou para fazer</p>
      <p>Lorem Ipsum é simplesmente uma simulação de texto da indústria tipográfica e de impressos, e vem sendo utilizado desde o século XVI, quando um impressor desconhecido pegou uma bandeja de tipos e os embaralhou para fazer</p>
      <p>Lorem Ipsum é simplesmente uma simulação de texto da indústria tipográfica e de impressos, e vem sendo utilizado desde o século XVI, quando um impressor desconhecido pegou uma bandeja de tipos e os embaralhou para fazer</p>
    </section>

    <div class="signature">
      <div class="signature-mark" role="img" aria-label="Assinatura manuscrita do responsável"></div>
      <div class="signature-name">Nome Responsável</div>
      <div class="signature-role">Cargo</div>
    </div>

    <footer class="contact">
      <div class="contact-item">
        <svg viewBox="0 0 24 24" aria-hidden="true"><path d="M6.6 10.8a15.1 15.1 0 0 0 6.6 6.6l2.2-2.2a1 1 0 0 1 1-.25 11.4 11.4 0 0 0 3.6.57 1 1 0 0 1 1 1V20a1 1 0 0 1-1 1A17 17 0 0 1 3 4a1 1 0 0 1 1-1h3.5a1 1 0 0 1 1 1c0 1.25.2 2.45.57 3.57a1 1 0 0 1-.25 1z"/></svg>
        <div>00 0000 00000<br>00 0000 00000</div>
      </div>
      <div class="contact-item">
        <svg viewBox="0 0 24 24" aria-hidden="true"><path d="M4 5h16a2 2 0 0 1 2 2v10a2 2 0 0 1-2 2H4a2 2 0 0 1-2-2V7a2 2 0 0 1 2-2zm0 2v.5l8 5 8-5V7zm0 2.8V17h16V9.8l-8 5z"/></svg>
        <div>VALDRANMETAL.COM.BR<br>CONTATO@VALDRANMETAL.COM.BR</div>
      </div>
      <div class="contact-item">
        <svg viewBox="0 0 24 24" aria-hidden="true"><path d="M12 2a7 7 0 0 0-7 7c0 5.2 7 13 7 13s7-7.8 7-13a7 7 0 0 0-7-7zm0 9.5A2.5 2.5 0 1 1 12 6.5a2.5 2.5 0 0 1 0 5z"/></svg>
        <div>NOME DA RUA, 000 - BAIRRO<br>CIDADE - ESTADO - CEP E PNS</div>
      </div>
    </footer>

    <svg class="footer-band" viewBox="0 0 780 52" preserveAspectRatio="none" aria-hidden="true">
      <path d="M0 20 Q0 8 20 8 L760 8 Q780 8 780 20 L780 52 L0 52 Z" fill="var(--brand-red)"/>
    </svg>
  </main>
</body>
</html>
```